New Dental Office Needs an Attractive and user friendly Website Designed

I need a website for a new dental office. The Name is Maplecrest Dentistry. I would like a Modern design with a user friendly interface and usability.
I would like a landing page, a page that lists the services we offer: Cosmetic Dentistry, Implants, Dental Hygiene, Emergency Services, Restorations, Dentures
Target Market(s)
Mid to upper class
Industry/Entity Type
Dentistry
Coding
Coded - Design and coding required
Number of Pages Required
1 page
Requirements
Must have
- Landing page that has a scheduling option, Procedures, operating hours, and contact us info
Nice to have
- Appealing design, Soft comforting colors. Easy to navigate page, Modern and professional.

```html
<!DOCTYPE html>
<html lang="en">
<head>
<meta charset="utf-8">
<title>Maplecrest Dentistry</title>
<link href="https://fonts.googleapis.com/css2?family=Gilda+Display&family=Outfit:wght@300;400;500;600&display=swap" rel="stylesheet">
<style>
:root{
  --orange:#f0b04a;
  --gold:#d8962f;
  --ink:#2d2d2d;
  --text:#3a3a3a;
  --grey-btn:#6b6b6b;
  --panel:#4a4848;
  --soft:#f4f5f7;
  --muted:#8a8a8a;
  --white:#fff;
}
*{margin:0;padding:0;box-sizing:border-box}
html,body{width:1200px;height:4360px;overflow:hidden}
body{position:relative;background:var(--white);font-family:"Outfit",sans-serif;color:var(--text)}
.abs{position:absolute}
.serif{font-family:"Gilda Display",serif;font-weight:400}
.btn{position:absolute;display:flex;align-items:center;justify-content:center;border-radius:30px;font-size:13px;font-weight:500;letter-spacing:1px;text-transform:uppercase;color:var(--white)}
.btn-grey{background:var(--grey-btn)}
.btn-orange{background:var(--orange)}
.photo{position:absolute}

/* header */
.site-header{position:absolute;top:0;left:0;width:1200px;height:86px;background:var(--white)}
.brand{position:absolute;font-family:"Gilda Display",serif;color:var(--ink);font-size:30px;line-height:1}
.brand small{display:block;font-size:14px;letter-spacing:4px;text-transform:uppercase;margin-top:4px;text-align:center}
.main-nav{position:absolute;left:378px;top:34px;display:flex;gap:37px;font-size:13px;letter-spacing:.5px;color:var(--ink)}
.header-phone{position:absolute;left:828px;top:24px;display:flex;align-items:center;gap:12px;font-weight:500;font-size:16px;color:var(--ink)}
.icon-circle{width:38px;height:38px;border-radius:50%;background:var(--grey-btn);display:flex;align-items:center;justify-content:center;flex:none}

/* hero */
.hero{position:absolute;top:86px;left:0;width:1200px;height:670px;background:linear-gradient(90deg,#efefef 0%,#e9e9e9 45%,#dcdde0 100%);overflow:hidden}
.hero-photo{left:480px;top:0;width:720px;height:670px;background:linear-gradient(100deg,rgba(233,233,233,0) 0%,#c9ccd2 30%,#8c97a8 60%,#d7d9dc 100%)}
.hero h1{position:absolute;left:110px;top:118px;color:var(--ink);line-height:.98}
.hero h1 .lead{font-size:60px;color:#555}
.hero h1 .big{font-size:70px}
.hero p{position:absolute;left:110px;top:336px;width:430px;font-size:17px;line-height:1.4;color:var(--ink)}

/* about */
.about-accent{left:52px;top:798px;width:318px;height:278px;background:var(--orange);border-radius:16px 16px 0 16px}
.about-text .eyebrow{position:absolute;left:643px;top:838px;font-size:15px;letter-spacing:3px;color:var(--gold)}
.section-title{color:var(--ink);line-height:1}
.about-title{position:absolute;left:636px;top:860px;font-size:58px}
.about-title span{color:#5a5a5a}
.rule{position:absolute;height:3px;background:var(--gold)}
.about-copy{position:absolute;left:637px;top:1008px;width:516px;font-size:18px;line-height:29px;color:var(--ink)}

/* services */
.services{position:absolute;top:1420px;left:0;width:1200px;height:808px;background:var(--soft)}
.services h2{position:absolute;left:0;width:1200px;top:48px;text-align:center;font-size:52px}
.card{position:absolute;width:326px;height:260px;border-radius:6px 34px 34px 6px;overflow:hidden;display:flex;align-items:flex-end;justify-content:center;padding-bottom:24px;color:var(--white);font-size:19px;font-weight:500;text-transform:uppercase}
.card-photo{background:linear-gradient(180deg,#cfd3d8 0%,#9aa1aa 60%,#5a5f66 100%)}
.card-feature{background:var(--gold);flex-direction:column;align-items:center;justify-content:flex-start;padding:38px 28px 0;text-align:center}
.card-feature h3{font-size:19px;font-weight:500}
.card-feature p{font-size:16px;line-height:1.15;text-transform:none;font-weight:400;margin-top:6px}
.card-feature .pill{margin-top:20px;background:#3e3e3e;border-radius:24px;padding:12px 36px;font-size:13px;font-weight:500;letter-spacing:.5px}

/* why */
.why{position:absolute;top:2228px;left:0;width:1200px;height:680px;background:#7c7c7c;overflow:hidden}
.why-photo{left:560px;top:0;width:640px;height:680px;background:linear-gradient(90deg,#7c7c7c 0%,#a8b3bd 35%,#c7d3dc 70%,#e2e8ec 100%)}
.why h2{position:absolute;left:108px;top:112px;font-size:58px;color:var(--white);line-height:1}
.why p{position:absolute;left:110px;top:260px;width:495px;font-size:19px;line-height:29px;color:var(--white)}

/* testimonials */
.testimonials h2{position:absolute;left:0;width:1200px;top:2930px;text-align:center;font-size:48px}
.arrow{position:absolute;width:44px;height:44px;border-radius:50%;display:flex;align-items:center;justify-content:center}
.review{position:absolute;top:3030px;height:272px;background:var(--white);box-shadow:0 6px 20px rgba(0,0,0,.08);padding:14px}
.review-inner{border:1px solid #e2e2e2;height:100%;padding:26px 30px 0;font-size:12.5px;line-height:21px;color:#555;position:relative}
.review-inner .quote{position:absolute;top:-18px;left:20px;font-family:"Gilda Display",serif;font-size:56px;color:#d5d5d5;line-height:1}
.review-inner .name{font-weight:600;color:#333;margin-top:12px;font-size:13px}
.stars{color:var(--orange);font-size:13px;letter-spacing:3px}
.badge{position:absolute;right:16px;bottom:14px;width:22px;height:22px;border-radius:50%;background:#cfcfcf}

/* contact */
.contact{position:absolute;top:3330px;left:0;width:1200px;height:655px;background:linear-gradient(180deg,#d08a25 0%,var(--gold) 40%,#d8962f 100%)}
.contact h2{position:absolute;left:128px;top:154px;font-size:50px;color:var(--white)}
.contact-item{position:absolute;left:125px;display:flex;gap:14px;color:var(--white)}
.contact-item .icon-circle{width:56px;height:56px;background:#9e6d2a}
.contact-item .label{font-size:18px}
.contact-item .value{font-size:20px;font-weight:500;line-height:1.25}
.booking{position:absolute;left:622px;top:160px;width:508px;height:410px;background:var(--panel);border-radius:70px 0 70px 0}
.booking h3{position:absolute;left:60px;top:46px;font-size:22px;letter-spacing:4px;color:var(--white);font-weight:500}
.field{position:absolute;height:40px;background:var(--white);display:flex;align-items:center;gap:8px;padding-left:16px;font-size:11px;color:#555}
.send{position:absolute;left:60px;top:310px;width:394px;height:48px;background:var(--orange);color:var(--white);display:flex;align-items:center;justify-content:center;gap:8px;font-size:14px;letter-spacing:2px;font-weight:500}

/* footer */
.footer-col{position:absolute;top:4052px}
.footer-col h4{font-size:16px;font-weight:500;color:var(--ink);letter-spacing:.5px;border-left:2px solid var(--ink);padding-left:10px;line-height:1}
.footer-col ul{list-style:none;margin-top:12px;padding-left:16px}
.footer-col li{font-size:13px;color:#555;line-height:28.5px}
.touch-row{display:flex;gap:14px;align-items:center;font-size:12.5px;color:#555;margin-top:14px}
.touch-row .ico{width:16px;display:flex;justify-content:center}
.touch-row .sep{border-left:1px solid #ccc;padding-left:10px;line-height:20px}
.social{position:absolute;top:4147px;width:22px;height:22px;border-radius:50%;background:var(--ink)}
.legal{position:absolute;top:4310px;font-size:12px;color:#999}
</style>
</head>
<body>

<header class="site-header">
  <div class="brand" style="left:116px;top:14px">Maplecrest<small>— Dentistry —</small></div>
  <nav class="main-nav"><span>ABOUT US</span><span>SERVICES</span><span>REVIEW</span><span>CONTACT US</span></nav>
  <div class="header-phone">
    <span class="icon-circle"><svg width="16" height="16" viewBox="0 0 24 24" fill="#fff"><path d="M6.6 10.8a15 15 0 0 0 6.6 6.6l2.2-2.2c.3-.3.7-.4 1-.2 1.1.4 2.3.6 3.6.6.6 0 1 .4 1 1V20c0 .6-.4 1-1 1A17 17 0 0 1 3 4c0-.6.4-1 1-1h3.5c.6 0 1 .4 1 1 0 1.3.2 2.5.6 3.6.1.3 0 .7-.2 1z"/></svg></span>
    (555) 402 1187
  </div>
  <div class="btn btn-orange" style="left:1030px;top:25px;width:140px;height:38px">Book Now</div>
</header>

<section class="hero">
  <div class="photo hero-photo" role="img" aria-label="Smiling senior patient in a dental chair with a dentist holding a mirror"></div>
  <h1 class="serif"><span class="lead">We Provide</span><br><span class="big">Exceptional<br>Dental Care</span></h1>
  <p>Lorem ipsum dolor sit amet, consectetur adipiscing elit, sed do eiusmod tempor incididunt</p>
  <div class="btn btn-grey" style="left:110px;top:406px;width:125px;height:48px">Book Now ›</div>
  <div class="btn btn-orange" style="left:296px;top:406px;width:172px;height:48px">View Services ›</div>
  <svg class="abs" style="left:0;top:510px" width="1200" height="160" viewBox="0 0 1200 160">
    <path d="M0,20 Q600,275 1200,20 L1200,160 L0,160 Z" fill="#fff"/>
    <path d="M0,20 Q600,275 1200,20" fill="none" stroke="#f0b04a" stroke-width="5"/>
  </svg>
</section>
<div class="abs" style="left:572px;top:697px;width:56px;height:56px;border-radius:50%;background:#fff;box-shadow:0 4px 12px rgba(0,0,0,.12)"></div>

<section class="about">
  <div class="abs about-accent"></div>
  <div class="photo" role="img" aria-label="Smiling woman at a dental check-up" style="left:65px;top:812px;width:475px;height:403px;border-radius:16px;background:linear-gradient(135deg,#d9d2cc,#b7aaa2 50%,#6d7fb8)"></div>
  <div class="photo" role="img" aria-label="Dentist pointing at a dental model on a desk" style="left:278px;top:1078px;width:306px;height:262px;border:6px solid #fff;border-radius:14px;background:linear-gradient(135deg,#dfe3e6,#b9c2c8 60%,#e9b7a9)"></div>
  <div class="about-text">
    <div class="eyebrow">WHO WE ARE</div>
    <h2 class="serif section-title about-title">About Maplecrest<br><span>Dentistry</span></h2>
    <div class="rule" style="left:637px;top:980px;width:60px"></div>
    <p class="about-copy">Lorem ipsum dolor sit amet, consectetur adipiscing elit, sed do eiusmod tempor incididunt ut labore et dolore magna aliqua. Ut enim ad minim veniam, quis nostrud exercitation ullamco laboris nisi ut aliquip ex ea commodo consequat. Duis aute irure dolor in reprehenderit in voluptate velit esse cillum dolore eu fugiat nulla pariatur. Excepteur sint occaecat cupidatat non proident, sunt in culpa qui officia deserunt</p>
    <div class="btn btn-grey" style="left:630px;top:1262px;width:172px;height:48px">Learn More ›</div>
  </div>
</section>

<section class="services">
  <h2 class="serif section-title">Our Services</h2>
  <div class="rule" style="left:560px;top:117px;width:80px"></div>
  <div class="card card-photo" style="left:90px;top:162px" role="img" aria-label="Woman receiving cosmetic dental care">Cosmetic Dentistry</div>
  <div class="card card-feature" style="left:436px;top:162px">
    <h3>Implants</h3>
    <p>Lorem ipsum dolor sit amet, consectetur adipiscing elit, sed do eiusmod tempor incididunt ut labore et dolore</p>
    <span class="pill">BOOK APPOINTMENT ›</span>
  </div>
  <div class="card card-photo" style="left:784px;top:162px" role="img" aria-label="Smiling woman during a dental hygiene visit">Dental Hygiene</div>
  <div class="card card-photo" style="left:90px;top:442px" role="img" aria-label="Man holding his cheek with tooth pain">Emergency Services</div>
  <div class="card card-photo" style="left:436px;top:442px;background:linear-gradient(180deg,#e7b3ae,#b56f6a 60%,#5d4a48)" role="img" aria-label="Close-up of a restored tooth">Restorations</div>
  <div class="card card-photo" style="left:784px;top:442px;background:linear-gradient(180deg,#ececec,#e8b7a2 55%,#6c6462)" role="img" aria-label="Hands holding a set of dentures">Dentures</div>
</section>

<section class="why">
  <div class="photo why-photo" role="img" aria-label="Dentist examining a laughing patient's teeth"></div>
  <h2 class="serif">Why Choose<br>Maplecrest</h2>
  <div class="rule" style="left:110px;top:246px;width:40px;background:#fff"></div>
  <p>Lorem ipsum dolor sit amet, consectetur adipiscing elit, sed do eiusmod tempor incididunt ut labore et dolore magna aliqua. Ut enim ad minim veniam, quis nostrud exercitation ullamco laboris nisi ut aliquip ex ea commodo consequat. Duis aute irure dolor in reprehenderit in voluptate velit esse cillum dol</p>
  <div class="btn" style="left:105px;top:467px;width:173px;height:44px;background:#8f8f8f">Learn More ›</div>
  <svg class="abs" style="left:0;top:600px" width="1200" height="80" viewBox="0 0 1200 80"><path d="M0,80 L0,75 Q600,-5 1200,32 L1200,80 Z" fill="#fff"/></svg>
</section>

<section class="testimonials">
  <h2 class="serif section-title">What Patient Says</h2>
  <div class="rule" style="left:565px;top:2985px;width:70px"></div>
  <div class="arrow" style="left:944px;top:2936px;border:1px solid #e0e0e0"><svg width="16" height="16" viewBox="0 0 24 24" fill="none" stroke="#bbb" stroke-width="2"><path d="M19 12H5M11 6l-6 6 6 6"/></svg></div>
  <div class="arrow" style="left:1000px;top:2936px;background:#5a5a5a"><svg width="16" height="16" viewBox="0 0 24 24" fill="none" stroke="#fff" stroke-width="2"><path d="M5 12h14M13 6l6 6-6 6"/></svg></div>
  <div class="photo" role="img" aria-label="Cheerful young woman in a pink sweater pointing at her smile" style="left:65px;top:2955px;width:350px;height:470px;background:linear-gradient(180deg,#fff 0%,#f1d9cc 35%,#e9a9c2 80%);border-radius:0 0 40px 0"></div>
  <div class="review" style="left:410px;width:280px"><div class="review-inner"><span class="quote">“</span>Lorem ipsum dolor sit amet, consectetur adipiscing elit, sed do eiusmod tempor incididunt ut labore et dolore magna aliqua Quis ipsum suspendisse ultrices gravida. Risus commodo viverra maecenas accumsan lacus vel facilisi<div class="name">Customer Name</div><div class="stars">★★★★★</div><span class="badge"></span></div></div>
  <div class="review" style="left:722px;width:284px"><div class="review-inner"><span class="quote">“</span>Lorem ipsum dolor sit amet, consectetur adipiscing elit, sed do eiusmod tempor incididunt ut labore et dolore magna aliqua Quis ipsum suspendisse ultrices gravida. Risus commodo viverra maecenas accumsan lacus vel facilisi<div class="name">Customer Name</div><div class="stars">★★★★★</div><span class="badge"></span></div></div>
  <div class="review" style="left:1040px;width:284px"><div class="review-inner"><span class="quote">“</span>Lorem ipsum dolor sit amet, consectetur adipiscing elit, sed do eiusmod tempor incididunt ut labore et dolore magna aliqua Quis ipsum suspendisse ultrices gravida. Risus commodo viverra maecenas accumsan lacus vel facilisi<div class="name">Customer Name</div><div class="stars">★★★★★</div></div></div>
</section>

<section class="contact">
  <svg class="abs" style="left:0;top:0" width="1200" height="110" viewBox="0 0 1200 110"><path d="M0,0 L1200,0 L1200,62 C950,100 620,110 420,82 C250,58 120,4 0,14 Z" fill="#fff"/></svg>
  <div class="photo" role="img" aria-label="Cheerful young woman in a pink sweater, lower part" style="left:65px;top:0;width:350px;height:95px;background:linear-gradient(180deg,#e9a9c2,#e2a0b8);border-radius:0 0 40px 0"></div>
  <h2 class="serif">Contact us</h2>
  <div class="contact-item" style="top:246px">
    <span class="icon-circle"><svg width="22" height="22" viewBox="0 0 24 24" fill="#fff"><path d="M12 2a7 7 0 0 0-7 7c0 5 7 13 7 13s7-8 7-13a7 7 0 0 0-7-7zm0 9.5A2.5 2.5 0 1 1 12 6.5a2.5 2.5 0 0 1 0 5z"/></svg></span>
    <div><div class="label">Address</div><div class="value">482 Harbor Lane - Suite 210<br>Brookhaven, Georgia 30319</div></div>
  </div>
  <div class="contact-item" style="top:375px">
    <span class="icon-circle"><svg width="22" height="22" viewBox="0 0 24 24" fill="#fff"><path d="M6.6 10.8a15 15 0 0 0 6.6 6.6l2.2-2.2c.3-.3.7-.4 1-.2 1.1.4 2.3.6 3.6.6.6 0 1 .4 1 1V20c0 .6-.4 1-1 1A17 17 0 0 1 3 4c0-.6.4-1 1-1h3.5c.6 0 1 .4 1 1 0 1.3.2 2.5.6 3.6.1.3 0 .7-.2 1z"/></svg></span>
    <div><div class="label">Phone</div><div class="value">555.214.3380</div></div>
  </div>
  <div class="contact-item" style="top:477px">
    <span class="icon-circle"><svg width="22" height="22" viewBox="0 0 24 24"><path d="M3 6h18v12H3zM3 6l9 7 9-7" fill="#fff" stroke="#9e6d2a" stroke-width="1.5"/></svg></span>
    <div><div class="label">Email address</div><div class="value">hello@maplecrestdental.com</div></div>
  </div>
  <div class="booking">
    <h3>BOOK APPOINTMENT</h3>
    <div class="field" style="left:60px;top:98px;width:193px">👤 First Name</div>
    <div class="field" style="left:261px;top:98px;width:193px">👤 Last Name</div>
    <div class="field" style="left:60px;top:150px;width:193px">✉ Email address</div>
    <div class="field" style="left:261px;top:150px;width:193px">☏ Phone</div>
    <div class="field" style="left:60px;top:204px;width:394px;height:94px;align-items:flex-start;padding-top:12px">✎ Message</div>
    <div class="send">SEND MESSAGE <svg width="14" height="14" viewBox="0 0 24 24" fill="none" stroke="#fff" stroke-width="2.5"><path d="M5 12h14M13 6l6 6-6 6"/></svg></div>
  </div>
</section>

<footer>
  <div class="brand" style="left:128px;top:4055px;font-size:38px">Maplecrest<small style="font-size:17px">— Dentistry —</small></div>
  <span class="social" style="left:144px"></span>
  <span class="social" style="left:193px"></span>
  <span class="social" style="left:241px"></span>
  <span class="social" style="left:287px"></span>
  <div class="footer-col" style="left:398px"><h4>NAVIGATION</h4><ul><li>Home</li><li>About</li><li>Services</li><li>Treatments</li><li>Fees</li></ul></div>
  <div class="footer-col" style="left:618px"><h4>RESOURCES</h4><ul><li>Book Appointment</li><li>Terms of Use</li><li>Privacy Policy</li><li>Reviews</li><li>Contact</li></ul></div>
  <div class="footer-col" style="left:832px"><h4>GET IN TOUCH</h4>
    <div class="touch-row" style="margin-top:18px"><span class="ico"><svg width="14" height="14" viewBox="0 0 24 24" fill="#2d2d2d"><path d="M12 2a7 7 0 0 0-7 7c0 5 7 13 7 13s7-8 7-13a7 7 0 0 0-7-7zm0 9.5A2.5 2.5 0 1 1 12 6.5a2.5 2.5 0 0 1 0 5z"/></svg></span><span class="sep">88 Willow Avenue Fairview,<br>OR 97024 USA</span></div>
    <div class="touch-row"><span class="ico"><svg width="14" height="14" viewBox="0 0 24 24" fill="#2d2d2d"><path d="M6.6 10.8a15 15 0 0 0 6.6 6.6l2.2-2.2c.3-.3.7-.4 1-.2 1.1.4 2.3.6 3.6.6.6 0 1 .4 1 1V20c0 .6-.4 1-1 1A17 17 0 0 1 3 4c0-.6.4-1 1-1h3.5c.6 0 1 .4 1 1 0 1.3.2 2.5.6 3.6.1.3 0 .7-.2 1z"/></svg></span><span class="sep">(555) 402 1187</span></div>
    <div class="touch-row"><span class="ico"><svg width="14" height="14" viewBox="0 0 24 24"><path d="M3 6h18v12H3z" fill="#2d2d2d"/><path d="M3 6l9 7 9-7" fill="none" stroke="#fff" stroke-width="1.5"/></svg></span><span class="sep">contact@maplecrestdental.com</span></div>
    <div class="touch-row"><span class="ico"><svg width="14" height="14" viewBox="0 0 24 24" fill="none" stroke="#2d2d2d" stroke-width="2.5"><circle cx="12" cy="12" r="9"/><path d="M12 7v5l3 2"/></svg></span><span class="sep">Mon – Fri 8am – 6pm · Sat 9am – 2pm</span></div>
  </div>
  <div class="abs" style="left:0;top:4284px;width:1200px;height:1px;background:#e2e2e2"></div>
  <div class="legal" style="left:112px">© 2025 Maplecrest Dentistry. All Rights Reserved</div>
  <div class="legal" style="left:808px;word-spacing:2px">Terms of use &nbsp;&nbsp;&nbsp; Privacy Policy &nbsp;&nbsp;&nbsp; Sitemap</div>
</footer>

</body>
</html>
```